BrightKeel Business Card Contest

We are looking for a modern business card that catches attention and is unique. Attached is the brand guide and logo files. Please note that the back side (not the side with our name and info) with be UV raise printed, so have fun with the design there. We want to include Name, Title, Phone number, email, website.

Contact Information for Business Card

Please see project description

```html
<!DOCTYPE html>
<html lang="en">
<head>
<meta charset="utf-8">
<title>BrightKeel Business Card</title>
<link rel="stylesheet" href="https://fonts.googleapis.com/css2?family=Poppins:wght@400;500;700&display=swap">
<style>
  :root {
    --backdrop: #d9d8d4;
    --card-white: #ffffff;
    --card-dark: #212329;
    --ink: #1d1e22;
    --ink-soft: #6b6d72;
    --blue-deep: #0d3a8c;
    --cyan: #1fbde6;
    --mist: #c9d4e0;
    --orange: #f08a1c;
    --red: #e0301e;
    --accent-stripe: linear-gradient(90deg, var(--blue-deep) 0%, var(--cyan) 35%, var(--mist) 55%, var(--orange) 80%, var(--red) 100%);
  }
  * { box-sizing: border-box; margin: 0; padding: 0; }
  html, body { width: 1200px; height: 801px; overflow: hidden; }
  body {
    background: var(--backdrop);
    font-family: "Poppins", sans-serif;
    display: flex;
    align-items: center;
    justify-content: center;
    gap: 40px;
  }
  .card {
    position: relative;
    width: 540px;
    height: 309px;
    box-shadow: 0 10px 28px rgba(0,0,0,0.18);
    overflow: hidden;
  }
  .card::after {
    content: "";
    position: absolute;
    left: 0; right: 0; bottom: 0;
    height: 9px;
    background: var(--accent-stripe);
  }
  .card--front { background: var(--card-white); }
  .card--back { background: var(--card-dark); }

  .front-brand {
    position: absolute;
    left: 48px;
    top: 118px;
    display: flex;
    align-items: center;
    gap: 12px;
  }
  .brand-square {
    width: 30px;
    height: 30px;
    background: var(--cyan);
  }
  .brand-name {
    font-weight: 500;
    font-size: 38px;
    letter-spacing: -0.5px;
    color: var(--ink);
    line-height: 1;
  }
  .divider {
    position: absolute;
    left: 300px;
    top: 90px;
    width: 2px;
    height: 112px;
    background: linear-gradient(180deg, var(--blue-deep), var(--cyan) 45%, var(--orange) 80%, var(--red));
  }
  .contact {
    position: absolute;
    left: 322px;
    top: 82px;
  }
  .contact__name {
    font-weight: 700;
    font-size: 17px;
    letter-spacing: 0.6px;
    color: var(--ink);
    text-transform: uppercase;
  }
  .contact__title {
    font-size: 13px;
    color: var(--ink-soft);
    margin-bottom: 14px;
  }
  .contact__list { list-style: none; }
  .contact__item {
    display: flex;
    align-items: center;
    gap: 8px;
    font-size: 13px;
    color: var(--ink-soft);
    line-height: 1.7;
  }
  .contact__item svg { width: 12px; height: 12px; flex: none; }

  .back-name {
    position: absolute;
    right: 40px;
    bottom: 58px;
    font-weight: 500;
    font-size: 46px;
    letter-spacing: -0.5px;
    color: var(--card-white);
    line-height: 1;
  }
</style>
</head>
<body>
  <section class="card card--front" aria-label="Business card front">
    <div class="front-brand">
      <span class="brand-square" aria-hidden="true"></span>
      <span class="brand-name">BrightKeel</span>
    </div>
    <div class="divider" aria-hidden="true"></div>
    <div class="contact">
      <p class="contact__name">Daniel Marlow</p>
      <p class="contact__title">President</p>
      <ul class="contact__list">
        <li class="contact__item">
          <svg viewBox="0 0 24 24" aria-hidden="true"><path fill="#1a73d9" d="M6.6 10.8a15 15 0 0 0 6.6 6.6l2.2-2.2a1 1 0 0 1 1-.25 11.4 11.4 0 0 0 3.6.57 1 1 0 0 1 1 1V20a1 1 0 0 1-1 1A17 17 0 0 1 3 4a1 1 0 0 1 1-1h3.5a1 1 0 0 1 1 1c0 1.25.2 2.45.57 3.57a1 1 0 0 1-.25 1z"/></svg>
          012-555-0148
        </li>
        <li class="contact__item">
          <svg viewBox="0 0 24 24" aria-hidden="true"><rect x="2" y="5" width="20" height="14" rx="1.5" fill="#f08a1c"/><path d="M2.5 6 12 13l9.5-7" fill="none" stroke="#fff" stroke-width="1.8"/></svg>
          info@brightkeel.com
        </li>
        <li class="contact__item">
          <svg viewBox="0 0 24 24" aria-hidden="true"><circle cx="12" cy="12" r="10" fill="#e0301e"/><g fill="none" stroke="#fff" stroke-width="1.3"><ellipse cx="12" cy="12" rx="4.5" ry="10"/><path d="M2 12h20M4 7h16M4 17h16"/></g></svg>
          www.brightkeel.com
        </li>
      </ul>
    </div>
  </section>

  <section class="card card--back" aria-label="Business card back">
    <span class="back-name">BrightKeel</span>
  </section>
</body>
</html>
```